Business Card

Edit current business card design

Need business card design where Business Name, Logo, Address, phone and fax, website address are permanent.Need to be able to add and edit employee name and email address.

Industry/Entity Type

Business

```html
<!DOCTYPE html>
<html lang="en">
<head>
<meta charset="utf-8">
<title>Marlow's Accounting Services – Business Card</title>
<link rel="stylesheet" href="https://fonts.googleapis.com/css2?family=Open+Sans:wght@400;600;700&display=swap">
<style>
  :root {
    --backdrop: #3b312d;
    --green: #2f6b46;
    --green-dark: #1f4d31;
    --green-light: #5f9a74;
    --ink: #1d1d1d;
    --card-white: #ffffff;
    --card-grey: #e6e7e6;
    --mark-grey: #d3d6d4;
  }
  * { margin: 0; padding: 0; box-sizing: border-box; }
  html, body {
    width: 1200px; height: 844px; overflow: hidden;
    background: var(--backdrop);
    font-family: "Open Sans", Arial, sans-serif;
  }
  .canvas {
    width: 1200px; height: 844px;
    display: flex; align-items: center; justify-content: center; gap: 50px;
  }
  .card {
    position: relative; width: 525px; height: 300px; overflow: hidden;
    box-shadow: 0 10px 24px rgba(0,0,0,.45);
  }

  /* Front: contact side */
  .card-front {
    background: linear-gradient(100deg, var(--card-grey) 0%, #f4f4f4 60%, #ffffff 100%);
  }
  .card-front .band {
    position: absolute; left: 0; right: 0; height: 16px;
    background: linear-gradient(180deg, var(--green-light), var(--green-dark));
  }
  .card-front .band-top { top: 0; }
  .card-front .band-bottom { bottom: 0; }
  .card-front .faint-mark {
    position: absolute; left: 118px; top: 40px; width: 215px; height: 215px;
    border-radius: 50%; background: var(--mark-grey); opacity: .6;
  }
  .contact {
    position: absolute; left: 0; right: 0; top: 44px; text-align: center; color: var(--ink);
  }
  .contact .person-name {
    display: inline-block; color: var(--green); font-weight: 700; font-size: 17px;
    letter-spacing: .5px; border-bottom: 1.5px solid var(--green); padding: 0 2px 1px;
  }
  .contact .credentials { font-size: 12px; margin-top: 2px; }
  .contact .details { margin-top: 30px; font-size: 14.5px; line-height: 19px; }
  .contact .address { margin-top: 16px; font-size: 14.5px; }

  /* Back: services side */
  .card-back { background: var(--card-white); }
  .card-back .tab {
    position: absolute; width: 22px; height: 46px;
    background: linear-gradient(90deg, var(--green-dark), var(--green-light));
  }
  .card-back .tab-right { right: 0; top: 26px; }
  .card-back .tab-left { left: 0; top: 178px; }
  .brand {
    position: absolute; left: 118px; top: 22px; display: flex; align-items: center; gap: 10px;
  }
  .brand .brand-dot {
    width: 56px; height: 56px; border-radius: 50%; background: var(--green);
  }
  .brand .brand-name {
    color: var(--green); font-weight: 700; font-size: 26px; letter-spacing: 3px; line-height: 1;
  }
  .brand .brand-sub {
    color: var(--green); font-weight: 400; font-size: 11px; letter-spacing: 1px; margin-top: 3px;
  }
  .services {
    position: absolute; left: 0; right: 0; top: 88px; text-align: center; color: var(--ink);
  }
  .services .services-title {
    display: inline-block; color: var(--green); font-weight: 600; font-size: 15px;
    border-bottom: 1.5px solid var(--green); margin-bottom: 4px;
  }
  .services ul { list-style: none; font-size: 13.5px; font-weight: 600; line-height: 18px; }
  .tagline {
    position: absolute; left: 0; right: 0; top: 252px; text-align: center;
    color: var(--green); font-weight: 700; font-size: 13.5px;
  }
</style>
</head>
<body>
<main class="canvas">

  <section class="card card-front" aria-label="Business card front">
    <div class="band band-top"></div>
    <div class="faint-mark"></div>
    <div class="contact">
      <div class="person-name">DEAN MARLOW</div>
      <div class="credentials">EA,ATA,ATP</div>
      <div class="details">
        <div>044-456-7890</div>
        <div>123-456-7890</div>
        <div>infoname@yourwebsite.com</div>
        <div>www.website.com</div>
      </div>
      <div class="address">1234 Address Tag Line | Country Name, AB | 123456</div>
    </div>
    <div class="band band-bottom"></div>
  </section>

  <section class="card card-back" aria-label="Business card back">
    <div class="tab tab-right"></div>
    <div class="tab tab-left"></div>
    <div class="brand">
      <div class="brand-dot"></div>
      <div>
        <div class="brand-name">MARLOW'S</div>
        <div class="brand-sub">Accounting Services</div>
      </div>
    </div>
    <div class="services">
      <div class="services-title">SERVICES</div>
      <ul>
        <li>Tax planning &amp; preparation for business &amp; individuals</li>
        <li>Tax problem resolutions</li>
        <li>Bookkeeping and Payroll Services</li>
        <li>Incorporation &amp; new business advisor</li>
        <li>Bookkeeping support &amp; training</li>
        <li>And more….</li>
      </ul>
    </div>
    <div class="tagline">Helping our Clients Keep More of What They Make</div>
  </section>

</main>
</body>
</html>
```